Velra Orchards Business Cards

design business cards for our new business should match my Copperline Quotes business cards

Contact Information for Business Card

2817 N 48th W Ave
Brenford, KS 60231

Requirements
Must have
• should match logo colors

```html
<!DOCTYPE html>
<html lang="en">
<head>
<meta charset="utf-8">
<title>Velra Orchards Business Cards</title>
<link href="https://fonts.googleapis.com/css2?family=Montserrat:wght@400;500;700;800&display=swap" rel="stylesheet">
<style>
  :root {
    --bg: #1e1e1e;
    --leaf-green: #7bc24a;
    --teal: #22b0b6;
    --mid-green: #45b68a;
    --deep-navy: #0c2e37;
    --paper: #ffffff;
    --ink: #183a44;
  }
  * { box-sizing: border-box; margin: 0; padding: 0; }
  html, body {
    width: 1200px; height: 988px; overflow: hidden;
    background: var(--bg);
    font-family: "Montserrat", sans-serif;
  }
  .card {
    position: absolute;
    width: 620px; height: 354px;
    border-radius: 18px;
    overflow: hidden;
    box-shadow: 0 18px 40px rgba(0,0,0,.55);
  }
  /* Back face */
  .card-back { left: 60px; top: 80px; }
  .card-back .pattern-field {
    position: absolute; inset: 0;
    background: linear-gradient(100deg, var(--leaf-green) 0%, var(--mid-green) 45%, var(--teal) 100%);
  }
  .card-back .brand {
    position: absolute; right: 48px; top: 148px;
    display: flex; align-items: center; gap: 12px;
    color: var(--paper); font-weight: 700; font-size: 34px; letter-spacing: .5px;
  }
  .brand .dot {
    width: 16px; height: 16px; border-radius: 50%; background: currentColor;
  }
  /* Front face */
  .card-front { left: 520px; top: 554px; background: var(--paper); }
  .card-front .bands { position: absolute; inset: 0; }
  .card-front .brand {
    position: absolute; left: 56px; top: 196px;
    display: flex; align-items: center; gap: 10px;
    color: var(--mid-green); font-weight: 700; font-size: 30px;
  }
  .identity {
    position: absolute; left: 360px; top: 78px; width: 230px;
    border-top: 1.5px solid var(--ink);
    border-bottom: 1.5px solid var(--ink);
    padding: 10px 0 12px;
  }
  .identity .name {
    font-weight: 800; font-size: 24px; color: var(--deep-navy); letter-spacing: .3px;
  }
  .identity .name .first { color: var(--leaf-green); }
  .identity .role { font-weight: 500; font-size: 16px; color: var(--leaf-green); margin-top: 2px; }
  .contact {
    position: absolute; left: 360px; top: 196px;
    list-style: none; font-size: 13px; color: var(--deep-navy); font-weight: 500;
  }
  .contact li { display: flex; align-items: flex-start; gap: 8px; margin-bottom: 5px; line-height: 1.3; }
  .contact svg { width: 13px; height: 13px; flex: none; margin-top: 2px; }
</style>
</head>
<body>

<section class="card card-back">
  <div class="pattern-field" role="img" aria-label="Green to teal gradient with faint repeating leaf pattern"></div>
  <div class="brand"><span class="dot"></span>Velra Orchards</div>
</section>

<section class="card card-front">
  <svg class="bands" viewBox="0 0 620 354" preserveAspectRatio="none" aria-hidden="true">
    <defs>
      <linearGradient id="bandGrad" x1="0" x2="1" y1="0" y2="0">
        <stop offset="0" stop-color="#7bc24a"/>
        <stop offset="1" stop-color="#22b0b6"/>
      </linearGradient>
    </defs>
    <polygon points="0,0 250,0 238,12 0,12" fill="#0c2e37"/>
    <polygon points="240,0 620,0 620,10 275,26 245,26" fill="url(#bandGrad)"/>
    <polygon points="0,330 440,330 470,322 620,322 620,354 0,354" fill="url(#bandGrad)"/>
    <polygon points="0,318 400,318 450,336 620,336 620,354 0,354" fill="#0c2e37"/>
  </svg>

  <div class="brand"><span class="dot"></span>Velra Orchards</div>

  <div class="identity">
    <div class="name"><span class="first">MARA</span> TELLEN</div>
    <div class="role">President</div>
  </div>

  <ul class="contact">
    <li>
      <svg viewBox="0 0 16 16"><path fill="#45b68a" d="M4 1l2.5 3-1.5 2a9 9 0 0 0 5 5l2-1.5 3 2.5-1.5 2.5C7 15 1 9 1.5 2.5z"/></svg>
      012-555-0147
    </li>
    <li>
      <svg viewBox="0 0 16 16"><rect x="1" y="3" width="14" height="10" rx="1" fill="#45b68a"/><path d="M1.5 3.5L8 9l6.5-5.5" stroke="#fff" stroke-width="1.2" fill="none"/></svg>
      tellen@velraorchards.com
    </li>
    <li>
      <svg viewBox="0 0 16 16"><circle cx="8" cy="8" r="6.5" fill="none" stroke="#45b68a" stroke-width="1.6"/><path d="M1.5 8h13M8 1.5c-3 3.5-3 9.5 0 13M8 1.5c3 3.5 3 9.5 0 13" stroke="#45b68a" stroke-width="1.2" fill="none"/></svg>
      www.velraorchards.com
    </li>
    <li>
      <svg viewBox="0 0 16 16"><path fill="#45b68a" d="M8 1a5 5 0 0 1 5 5c0 4-5 9-5 9S3 10 3 6a5 5 0 0 1 5-5z"/><circle cx="8" cy="6" r="2" fill="#fff"/></svg>
      <span>2817 N 48th W Ave Brenford,<br>KS 60231</span>
    </li>
  </ul>
</section>

</body>
</html>
```